Price list for young Relaxon clinic

I require a price list/Treatment menu for clinic

To include:
Logo
Address
Phone number
Website

List of services and Prices
Relaxon 1 area £100
Relaxon 2 areas £150
Relaxon 3 areas £200
Lip Enhancement 0.5ml £100
Lip Enhancement 1ml £200
Facial Fillers £200 per 1ml
Volumiq £450 per session (2 vials - must be bought as a course)
Non Surgical Face Lift (Thread Lift) £600 per area
Skin Press Full Face £250
Skin Press Small Per Small Area £100
Cryo Therapy £60
Chemical Peel Light Peel and Microdermabrasion £85
Chemical Peel Deep Peel £150
Consultation £30 redeemable against service
Relaxon Top Up Relaxon £50 (must be within 2 weeks of 1st treatment)
Filler Top Up £100 (must be within 2 weeks of 1st appointment)

Open Hours
Updates

Company Name: HVM Address: 482 Pellbrook Road, 6 Warnford High Street, KT4 3JQ Phone: 0208 947 2186 Website: www.hollyvanmereaesthetics.co.uk

Please add more colour

Needs to be much cleaner and simpler Front page to include logo and price list Back page to inculde open hours and contact information including google map. Please no images with needles. Images of lips and faces are good, but try not to crowd copy on the pagei. No copy on top of images. White, grey, black and reds are good on colouring.

Target Market(s)

young market ages 22-45 years old mainly female
modern

Industry/Entity Type

Clinic

Number of Pages Required

4 page

Requirements
Must have
• Logo - logo must be in colour grey/silver
• Address (small map?)
• Phone number
• Web address
• Services
• Open hours
• Prices
• Images

```html
<!DOCTYPE html>
<html lang="en">
<head>
<meta charset="utf-8">
<title>Holly Vanmere Aesthetics – Services &amp; Price List</title>
<link rel="stylesheet" href="https://fonts.googleapis.com/css2?family=Cormorant+Garamond:wght@500;600&family=Parisienne&family=Handlee&display=swap">
<style>
  :root {
    --paper: #ffffff;
    --grey: #9b9b9b;
    --grey-dark: #8a8a8a;
    --rule-grey: #e6e6e6;
    --blush: #f2c6cb;
    --blush-soft: #f7dfe1;
    --map-tone: #ecd5d5;
    --map-tone-deep: #dcb9bb;
  }
  * { margin: 0; padding: 0; box-sizing: border-box; }
  html, body { width: 1200px; height: 2732px; overflow: hidden; background: var(--paper); }
  .menu {
    position: relative; width: 1200px; height: 2732px;
    font-family: "Cormorant Garamond", Georgia, serif; color: var(--grey);
  }
  .brand { position: absolute; top: 40px; left: 0; width: 100%; text-align: center; }
  .brand-mark {
    display: block; width: 200px; height: 200px; margin: 0 auto;
    border-radius: 50%; background: var(--grey);
  }
  .brand-name {
    margin-top: 110px; font-weight: 600; color: var(--grey);
    letter-spacing: 6px; text-transform: uppercase; line-height: 1.05;
  }
  .brand-name .line-a { display: block; font-size: 52px; }
  .brand-name .line-b { display: block; font-size: 74px; }
  .rule { position: absolute; left: 91px; width: 1018px; height: 3px; background: var(--rule-grey); }
  .rule.blush { background: var(--blush-soft); }
  .rule.short { left: 376px; width: 454px; background: var(--blush-soft); }
  .tagline {
    position: absolute; top: 565px; width: 100%; text-align: center;
    font-size: 32px; font-weight: 600; color: var(--grey-dark);
  }
  .section-title {
    position: absolute; width: 100%; text-align: center;
    font-family: "Parisienne", cursive; font-size: 68px; color: var(--grey); line-height: 1;
  }
  .price-list { position: absolute; top: 815px; left: 0; width: 100%; list-style: none; text-align: center; }
  .price-list li { font-size: 35px; font-weight: 600; line-height: 61px; white-space: nowrap; }
  .price-list .note { font-size: 25px; }
  .visit { position: absolute; top: 2010px; left: 114px; width: 1000px; height: 380px; }
  .map {
    position: absolute; left: 0; top: 6px; width: 442px; height: 364px; border-radius: 50%;
    background: radial-gradient(ellipse at 45% 45%, var(--map-tone) 0%, var(--map-tone-deep) 100%);
  }
  .hours { position: absolute; left: 492px; top: 0; list-style: none; }
  .hours li { font-size: 34px; font-weight: 600; line-height: 48px; white-space: nowrap; }
  .hours .sep { color: var(--blush); padding: 0 6px; }
  .hours .note { display: block; font-size: 24px; line-height: 30px; margin: -4px 0 4px; }
  .contact {
    position: absolute; top: 2490px; width: 100%; text-align: center;
    font-family: "Handlee", cursive; font-size: 30px; color: var(--grey); line-height: 68px;
  }
  .contact .key { color: var(--blush); margin-right: 8px; }
  .contact .gap { display: inline-block; width: 22px; }
</style>
</head>
<body>
<main class="menu">
  <header class="brand">
    <span class="brand-mark"></span>
    <h1 class="brand-name"><span class="line-a">Holly Vanmere</span><span class="line-b">Aesthetics</span></h1>
  </header>

  <div class="rule" style="top:536px"></div>
  <p class="tagline">Achieve a fresh &amp; beautiful you</p>
  <div class="rule short" style="top:630px"></div>

  <h2 class="section-title" style="top:700px">Services &amp; Price List</h2>
  <ul class="price-list">
    <li>Relaxon 1 area £100</li>
    <li>Relaxon 2 areas £150</li>
    <li>Relaxon 3 areas £200</li>
    <li>Lip Enhancement 0.5ml £100</li>
    <li>Lip Enhancement 1ml £200</li>
    <li>Facial Fillers £200 per 1ml</li>
    <li>Volumiq £450 per session <span class="note">(2 vials - must be bought as a course)</span></li>
    <li>Non Surgical Face Lift (Thread Lift) £600 per area</li>
    <li>Skin Press Full Face £250</li>
    <li>Skin Press Small Per Small Area £100</li>
    <li>Cryo Therapy £60</li>
    <li>Chemical Peel Light Peel and Microdermabrasion £85</li>
    <li>Chemical Peel Deep Peel £150</li>
    <li>Consultation £30 redeemable against service</li>
    <li>Relaxon Top Up Relaxon £50 <span class="note">(must be within 2 weeks of 1st treatment)</span></li>
    <li>Filler Top Up £100 <span class="note">(must be within 2 weeks of 1st appointment)</span></li>
  </ul>

  <div class="rule blush" style="top:1826px"></div>
  <h2 class="section-title" style="top:1880px">Come &amp; visit us...</h2>

  <section class="visit">
    <div class="map" role="img" aria-label="Street map showing the clinic location on Warnford High Street"></div>
    <ul class="hours">
      <li>Monday<span class="sep">||</span>10am - 4pm</li>
      <li>Tuesday<span class="sep">||</span>10am - 4pm</li>
      <li>Wednesday<span class="sep">||</span>12pm - 8pm</li>
      <li>Thursday<span class="sep">||</span>7.30am - 4.30pm<span class="note">(@ number 9 Calloway Street only)</span></li>
      <li>Friday<span class="sep">||</span>10am - 2pm</li>
      <li>Saturday<span class="sep">||</span>9am - 2pm</li>
      <li>Sunday<span class="sep">||</span>Closed</li>
    </ul>
  </section>

  <div class="rule blush" style="top:2450px"></div>
  <address class="contact">
    <div><span class="key">A.</span>482 Pellbrook Road, 6 Warnford High Street, KT4 3JQ</div>
    <div><span class="key">P.</span>0208 947 2186<span class="gap"></span><span class="key">E.</span>hvmwarnfordbookings@mail.com</div>
    <div><span class="key">W.</span>www.hollyvanmereaesthetics.co.uk</div>
  </address>
</main>
</body>
</html>
```